Executive Business Consulting for Telco Companies and Telco Start up companies

1.) Looking for an appealing and action oriented business card design.
2.)The target companies to work with start-ups and existing companies that focus on Business to Business applications
3.) For "OKRA", a Belgium based Executive consultancy company specialised in global reach starting from the centre of Europe = Brussels.
4.) Our core competence is the Go To Market in All major global regions, incl North America, Latin America, Asia, Japan, Europe and Africa.
5.) Design should be appealing to CEO, CFO and Venture Funds signalling; Expertise, Stability, Maturity and Commitment
6.) Preferred color scheme is Blue focussed and using a modern FONT.
7.) Logo design is included (uploaded)

Target Market(s)

Telecommunication Market. Companies in a B2B business model, developping services or applications to make business run more profitable

Industry/Entity Type

Business

Contact Information for Business Card

Company Name: OKRA
Name: Joris Vandelay
Titel: Managing Director
Address: Kalkweg 58 , B-9170 Meerdonk , Belgium
Tel: + 32 471 208 364
Email: joris_vandelay@plimbox.example
LinkedIn: be.netprofilo.example/in/jorisvandelay/

Font styles to use
Serif

Colors
0455a3
3277b5

Requirements
Must have
• Second Side Text: Execute Sales Strategy and Transformation

```html
<!DOCTYPE html>
<html lang="en">
<head>
<meta charset="utf-8">
<title>OKRA Business Card</title>
<link rel="stylesheet" href="https://fonts.googleapis.com/css2?family=PT+Serif:wght@400;700&display=swap">
<style>
  :root {
    --stage: #5a5a58;
    --brand-blue: #0455a3;
    --brand-blue-light: #3277b5;
    --card-white: #ffffff;
    --ink-dark: #333333;
    --ink-navy: #1c3b6b;
    --ink-grey: #8c8c8c;
    --mark-navy: #2b3d63;
  }
  html, body {
    margin: 0;
    padding: 0;
    width: 1200px;
    height: 509px;
    overflow: hidden;
    background: var(--stage);
    font-family: "PT Serif", Georgia, serif;
  }
  .stage {
    position: relative;
    width: 1200px;
    height: 509px;
  }
  .card {
    position: absolute;
    border-radius: 18px;
    overflow: hidden;
  }
  .card-front {
    left: 95px;
    top: 113px;
    width: 507px;
    height: 293px;
    background: linear-gradient(180deg, #1a5fb0 0%, var(--brand-blue-light) 48%, var(--brand-blue) 100%);
  }
  .front-brand {
    position: absolute;
    left: 0;
    right: 0;
    top: 118px;
    display: flex;
    flex-direction: column;
    align-items: center;
    gap: 14px;
  }
  .front-logo {
    display: flex;
    align-items: center;
    gap: 14px;
  }
  .front-logo-dot {
    width: 36px;
    height: 36px;
    border-radius: 50%;
    background: var(--card-white);
  }
  .front-logo-name {
    color: var(--card-white);
    font-weight: 700;
    font-size: 42px;
    line-height: 1;
    letter-spacing: 1px;
  }
  .front-tagline {
    margin: 0;
    color: var(--card-white);
    font-size: 14px;
    letter-spacing: 0.4px;
  }
  .card-back {
    left: 620px;
    top: 111px;
    width: 508px;
    height: 293px;
    background: var(--card-white);
  }
  .holder-name {
    position: absolute;
    left: 30px;
    top: 58px;
    margin: 0;
    font-size: 18px;
    font-weight: 700;
    line-height: 24px;
    color: var(--ink-dark);
    letter-spacing: 0.3px;
  }
  .holder-title {
    position: absolute;
    left: 30px;
    top: 88px;
    margin: 0;
    font-size: 15.5px;
    line-height: 22px;
    color: var(--ink-navy);
  }
  .contact-list {
    position: absolute;
    left: 26px;
    top: 124px;
    margin: 0;
    padding: 0;
    list-style: none;
    font-size: 15.5px;
    line-height: 24px;
    color: var(--ink-grey);
  }
  .back-mark {
    position: absolute;
    left: 326px;
    top: 58px;
    width: 108px;
    height: 108px;
    border-radius: 50%;
    background: var(--mark-navy);
  }
</style>
</head>
<body>
  <main class="stage">
    <section class="card card-front" role="img" aria-label="Card front: blue field with soft oval pattern, OKRA name and tagline">
      <div class="front-brand">
        <div class="front-logo">
          <span class="front-logo-dot"></span>
          <span class="front-logo-name">OKRA</span>
        </div>
        <p class="front-tagline">Execute Sales Strategy and Transformation</p>
      </div>
    </section>

    <section class="card card-back" aria-label="Card back">
      <h1 class="holder-name">JORIS VANDELAY</h1>
      <p class="holder-title">Managing Director</p>
      <ul class="contact-list">
        <li>Address: Kalkweg 58 ,</li>
        <li>B-9170 Meerdonk , Belgium</li>
        <li>Tel: + 32 471 208 364</li>
        <li>Email: joris_vandelay@plimbox.example</li>
        <li>LinkedIn: be.netprofilo.example/in/jorisvandelay/</li>
      </ul>
      <div class="back-mark" aria-hidden="true"></div>
    </section>
  </main>
</body>
</html>
```